Home page design for Drone video business (the Business focusses on home videos for realtors)

Dear reader,

*I NEED DESIGNS OF ALL THE PAGES*
We need a first design of a homepage and of 4 other pages of the website of a business that sells drone video services. All the pages will need to be in the similar design style.
The video's are targeted at consumers that want to sell there home and would like to have a cool drone video of photos of their home.

How does the website look:
- has a navbar on top
- A cool looking banner of an areal drone.
- A Big header: with company name: SkyNestReels
- A smaller subheader: We film your home to increase your chances of sale
- Then a section with a Big header: How does it work
- In this section a place for a vimeo explainitory video
- Then a similar navbar styled bar with a phone number and a email address
- Then a section where the videos porfolio is displayed in a cool way
- Inside this sectiona header: Our work

- A section with header: Why us?
- 4 symbols here with a subheader and some lorum ipsum text underneath (see wireframe images)

- Under that a: Contact us
- where you can put in name, email, phone, message box and a send button

- At the bottom a footer with phone number and a fake address for now.

Be creative. Use creative but serious color.
Use a serious font. Make it a sharp design. Sharp lines. Not to dark design and not to light design.

The wireframes are the same kind of images.
PLEASE PUT IN DESIGNS OF ALL THE PAGES

Good luck

Target Market(s)

People that want to sell home and want to make a cool drone video or photos of their home.

Industry/Entity Type

Business

Contact Information for Business Card

Milo Brenning
milo@skynestreels.example
+31647283915

Logo Text

SkyNestReels

Number of Pages Required

1 page

Font styles to use
Sans Serif

Requirements
Must have
• All the sections as explained in the instructions.
• The nav bar should have an about us, services, portfolio and a contact us buttons.
• See instruction for details.
• Must include designs of the front page, contact us, our services, portfolio and contact us.
• If you do add some designs for the "about us", "services", "prices", "portfolio" and "contact us" pages, you make a way better chance of winning the competition.
Nice to have
• designs for the other pages as described at the Must haves. You make a better chance of winning if you include them. Look at the wireframes to see the mockups for those pages. think creative about what kind of sections and design should be included in those pages.
Should not have
• bad designs.

```html
<!DOCTYPE html>
<html lang="en">
<head>
<meta charset="utf-8">
<title>SkyNestReels – Home Drone Video</title>
<link rel="stylesheet" href="https://fonts.googleapis.com/css2?family=Source+Sans+3:wght@400;600;700&family=Open+Sans:wght@400;600&display=swap">
<style>
:root{
  --blue:#3fa3e8;
  --ink:#22252b;
  --text:#3a3a3a;
  --light:#f1f1f1;
  --white:#ffffff;
  --grey:#808080;
  --footer:#333333;
  --line:#dcdcdc;
}
*{box-sizing:border-box;margin:0;padding:0}
html,body{width:1200px;height:2510px;overflow:hidden}
body{position:relative;background:var(--light);font-family:"Open Sans",Arial,sans-serif;color:var(--text)}
.abs{position:absolute}
h1,h2,h3{font-family:"Source Sans 3",Arial,sans-serif;font-weight:700}

/* nav */
.site-nav{left:0;top:0;width:1200px;height:88px;background:var(--white);border-top:3px solid var(--blue)}
.brand{position:absolute;left:130px;top:26px;font-family:"Source Sans 3",sans-serif;font-weight:600;font-size:26px;color:var(--ink);letter-spacing:1px}
.nav-links{position:absolute;right:130px;top:38px;display:flex;gap:40px;list-style:none;font-size:11px;text-transform:uppercase;color:var(--ink)}
.nav-links .active{color:var(--blue)}

/* hero */
.hero{left:0;top:88px;width:1200px;height:472px;background:linear-gradient(180deg,#4e5a6c 0%,#6d7888 45%,#5d6570 78%,#3f3a30 100%)}
.hero h1{position:absolute;left:0;width:1200px;top:160px;text-align:center;font-size:70px;color:var(--white);letter-spacing:1px;text-shadow:0 3px 6px rgba(0,0,0,.35)}
.hero h1 span{color:var(--blue)}
.hero p{position:absolute;left:0;width:1200px;top:258px;text-align:center;font-family:"Source Sans 3",sans-serif;font-weight:700;font-size:18px;color:var(--white);text-transform:uppercase}
.round-arrow{position:absolute;width:28px;height:28px}

/* how */
.section-title{position:absolute;left:0;width:1200px;text-align:center;font-size:32px;color:var(--ink);text-transform:uppercase}
.section-title span{color:var(--blue)}
.section-title.on-dark{color:var(--white)}
.video-frame{left:308px;top:675px;width:583px;height:326px;background:radial-gradient(ellipse at 50% 55%,#8a8a80 0%,#5d7fc4 45%,#3c62b8 100%)}
.player-bar{position:absolute;left:11px;bottom:10px;width:561px;height:30px}

/* contact strip */
.contact-strip{left:0;top:1046px;width:1200px;height:62px;background:var(--blue);display:flex;justify-content:center;align-items:center;gap:34px;color:var(--white);font-size:17px}
.contact-item{display:flex;align-items:center;gap:9px}

/* work */
.work{left:0;top:1108px;width:1200px;height:402px;background:var(--grey)}
.thumb{position:absolute;top:108px;width:299px;height:216px;border:2px solid var(--white)}
.thumb .play{position:absolute;left:130px;top:88px}

/* why */
.feature{position:absolute;width:462px;height:144px;background:var(--white);border:1px solid var(--line)}
.feature .icon{position:absolute;left:9px;top:20px;width:86px;height:86px;border-radius:50%;background:var(--blue);display:flex;align-items:center;justify-content:center}
.feature h3{position:absolute;left:121px;top:20px;font-size:18px;color:var(--ink);text-transform:uppercase}
.feature p{position:absolute;left:121px;top:56px;width:322px;font-size:11px;line-height:19px;text-align:justify;color:var(--text)}

/* contact form */
.contact{left:0;top:1978px;width:1200px;height:440px;background:linear-gradient(160deg,#5aa2ee 0%,#2f7fe0 55%,#4c95ea 100%)}
.field{position:absolute;background:var(--white);border-radius:3px;font-size:10px;color:#333;padding:14px 12px}
.submit{position:absolute;left:548px;top:2339px;width:109px;height:35px;background:linear-gradient(#2a2a2a,#0e0e0e);color:var(--white);border-radius:3px;font-size:12px;text-transform:uppercase;display:flex;align-items:center;justify-content:center}

/* footer */
.site-footer{left:0;top:2418px;width:1200px;height:92px;background:var(--footer);color:var(--white)}
.site-footer .contact-item{font-size:17px}
.footer-line{position:absolute;left:0;top:22px;width:1200px;display:flex;justify-content:center;gap:34px}
.copyright{position:absolute;left:0;top:58px;width:1200px;text-align:center;font-size:10px;text-transform:uppercase}
</style>
</head>
<body>

<header class="site-nav abs">
  <div class="brand">SkyNestReels</div>
  <ul class="nav-links">
    <li class="active">Services</li>
    <li>About us</li>
    <li>Portfolio</li>
    <li>Contact</li>
  </ul>
</header>

<section class="hero abs" role="img" aria-label="Aerial drone with camera hovering under a cloudy sky above a field">
  <svg class="round-arrow" style="left:103px;top:201px" viewBox="0 0 28 28"><circle cx="14" cy="14" r="13" fill="none" stroke="#fff" stroke-width="1.3"/><path d="M16 8l-6 6 6 6" fill="none" stroke="#fff" stroke-width="1.5"/></svg>
  <svg class="round-arrow" style="left:1068px;top:201px" viewBox="0 0 28 28"><circle cx="14" cy="14" r="13" fill="none" stroke="#fff" stroke-width="1.3"/><path d="M12 8l6 6-6 6" fill="none" stroke="#fff" stroke-width="1.5"/></svg>
  <h1>SKY<span>NEST</span> REELS</h1>
  <p>We film your home to increase your chances of sale</p>
</section>

<h2 class="section-title" style="top:597px">How does it <span>work</span></h2>

<div class="video-frame abs" role="img" aria-label="Explainer video showing a close-up of a drone camera">
  <svg class="player-bar" viewBox="0 0 561 30">
    <rect x="0" y="0" width="52" height="30" rx="2" fill="#2b2f38"/>
    <path d="M21 8l12 7-12 7z" fill="#fff"/>
    <rect x="60" y="0" width="501" height="30" rx="2" fill="#2b2f38"/>
    <rect x="68" y="12" width="411" height="6" rx="3" fill="#4a5060"/>
    <rect x="68" y="12" width="80" height="6" rx="3" fill="#3fa3e8"/>
    <g fill="#3fa3e8"><rect x="490" y="10" width="2" height="10"/><rect x="494" y="10" width="2" height="10"/><rect x="498" y="10" width="2" height="10"/><rect x="502" y="10" width="2" height="10"/><rect x="506" y="10" width="2" height="10"/></g>
    <text x="516" y="20" font-family="Source Sans 3,sans-serif" font-weight="700" font-style="italic" font-size="11" fill="#3fa3e8">HD</text>
    <path d="M540 10h4v2h-2v2h-2zM550 10h4v4h-2v-2h-2zM540 16h2v2h2v2h-4zM552 16h2v4h-4v-2h2z" fill="#fff"/>
  </svg>
</div>

<div class="contact-strip abs">
  <span class="contact-item">
    <svg width="16" height="16" viewBox="0 0 16 16"><path d="M3.5 1.5l2.5 3-1.5 2c.8 1.8 2.3 3.3 4 4l2-1.5 3 2.5-1.5 2.5C6.5 14 2 9.5 1 3z" fill="#fff"/></svg>
    + 31 647283915
  </span>
  <span class="contact-item">
    <svg width="18" height="14" viewBox="0 0 18 14"><rect x="1" y="1" width="16" height="12" fill="none" stroke="#fff" stroke-width="1.5"/><path d="M1 1l8 7 8-7" fill="none" stroke="#fff" stroke-width="1.5"/></svg>
    CONTACT @SKYNESTREELS.EXAMPLE
  </span>
</div>

<section class="work abs">
  <h2 class="section-title on-dark" style="top:38px">Our work</h2>
  <svg class="round-arrow" style="left:87px;top:201px" viewBox="0 0 28 28"><circle cx="14" cy="14" r="13" fill="none" stroke="#fff" stroke-width="1.3"/><path d="M16 8l-6 6 6 6" fill="none" stroke="#fff" stroke-width="1.5"/></svg>
  <svg class="round-arrow" style="left:1084px;top:201px" viewBox="0 0 28 28"><circle cx="14" cy="14" r="13" fill="none" stroke="#fff" stroke-width="1.3"/><path d="M12 8l6 6-6 6" fill="none" stroke="#fff" stroke-width="1.5"/></svg>

  <div class="thumb" style="left:133px;background:linear-gradient(135deg,#5a5a5a,#2e2e2e 60%,#474340)" role="img" aria-label="White quadcopter drone indoors">
    <svg class="play" width="36" height="36" viewBox="0 0 36 36"><circle cx="18" cy="18" r="17" fill="rgba(0,0,0,.55)"/><path d="M14 11l11 7-11 7z" fill="#fff"/></svg>
  </div>
  <div class="thumb" style="left:450px;background:linear-gradient(180deg,#8fbbe6 0%,#b9d3ec 45%,#5f8a4a 100%)" role="img" aria-label="Camera drone flying beside a house">
    <svg class="play" width="36" height="36" viewBox="0 0 36 36"><circle cx="18" cy="18" r="17" fill="rgba(0,0,0,.55)"/><path d="M14 11l11 7-11 7z" fill="#fff"/></svg>
  </div>
  <div class="thumb" style="left:770px;background:linear-gradient(180deg,#5b95de,#8ab6ec)" role="img" aria-label="Hexacopter drone against a blue sky">
    <svg class="play" width="36" height="36" viewBox="0 0 36 36"><circle cx="18" cy="18" r="17" fill="rgba(0,0,0,.55)"/><path d="M14 11l11 7-11 7z" fill="#fff"/></svg>
  </div>
</section>

<h2 class="section-title" style="top:1552px">Why <span>us?</span></h2>

<article class="feature" style="left:133px;top:1625px">
  <div class="icon"><svg width="44" height="50" viewBox="0 0 44 50"><text x="22" y="42" text-anchor="middle" font-family="Source Sans 3,sans-serif" font-size="50" fill="#fff">$</text></svg></div>
  <h3>Cheap</h3>
  <p>Nemo enim ipsam voluptatem quia voluptas sit aspernatur aut odit aut fugit, sed quia consequuntur magni dolores eos qui ratione voluptatem sequi nesciunt.</p>
</article>
<article class="feature" style="left:605px;top:1625px">
  <div class="icon"><svg width="48" height="32" viewBox="0 0 48 32"><rect x="2" y="3" width="30" height="26" rx="4" fill="#fff"/><path d="M34 13l12-8v22l-12-8z" fill="#fff"/></svg></div>
  <h3>Flexible</h3>
  <p>Nemo enim ipsam voluptatem quia voluptas sit aspernatur aut odit aut fugit, sed quia consequuntur magni dolores eos qui ratione voluptatem sequi nesciunt.</p>
</article>
<article class="feature" style="left:133px;top:1785px">
  <div class="icon"><svg width="44" height="44" viewBox="0 0 44 44"><circle cx="22" cy="22" r="19" fill="#fff"/><path d="M13 12c4 1 6 4 5 7s-4 2-4 6 3 5 2 8M28 8c-2 3 0 6 3 6s4 4 2 7-5 2-5 6 2 5 1 8" fill="none" stroke="#3fa3e8" stroke-width="3"/></svg></div>
  <h3>9K Quality</h3>
  <p>Nemo enim ipsam voluptatem quia voluptas sit aspernatur aut odit aut fugit, sed quia consequuntur magni dolores eos qui ratione voluptatem sequi nesciunt.</p>
</article>
<article class="feature" style="left:605px;top:1785px">
  <div class="icon"><svg width="46" height="40" viewBox="0 0 46 40"><path d="M3 3v34h40" fill="none" stroke="#fff" stroke-width="3"/><path d="M9 30l10-11 7 7 13-14" fill="none" stroke="#fff" stroke-width="3.5"/><path d="M32 10h9v9" fill="none" stroke="#fff" stroke-width="3.5"/></svg></div>
  <h3 style="left:135px">Increase sale chance</h3>
  <p style="left:135px;width:312px">Nemo enim ipsam voluptatem quia voluptas sit aspernatur aut odit aut fugit, sed quia consequuntur magni dolores eos qui ratione voluptatem sequi nesciunt.</p>
</article>

<section class="contact abs" role="img" aria-label="Blue-tinted aerial view of a drone over a tree-lined landscape">
  <h2 class="section-title on-dark" style="top:40px">Contact us</h2>
</section>
<div class="field" style="left:373px;top:2090px;width:221px;height:42px">Name</div>
<div class="field" style="left:605px;top:2090px;width:221px;height:42px">Email</div>
<div class="field" style="left:373px;top:2137px;width:221px;height:42px">Phone</div>
<div class="field" style="left:373px;top:2187px;width:453px;height:137px">Message</div>
<div class="submit">Submit</div>

<footer class="site-footer abs">
  <div class="footer-line">
    <span class="contact-item">
      <svg width="16" height="16" viewBox="0 0 16 16"><path d="M3.5 1.5l2.5 3-1.5 2c.8 1.8 2.3 3.3 4 4l2-1.5 3 2.5-1.5 2.5C6.5 14 2 9.5 1 3z" fill="#fff"/></svg>
      + 31 647283915
    </span>
    <span class="contact-item">
      <svg width="18" height="14" viewBox="0 0 18 14"><rect x="1" y="1" width="16" height="12" fill="none" stroke="#fff" stroke-width="1.5"/><path d="M1 1l8 7 8-7" fill="none" stroke="#fff" stroke-width="1.5"/></svg>
      CONTACT @SKYNESTREELS.EXAMPLE
    </span>
  </div>
  <p class="copyright">© 2016 SkyNestReels. All rights reserved.</p>
</footer>

</body>
</html>
```